Telecommunications/Power civil contractor needs business card design

Were a new telecommunications/power underground civil contractor that is looking for a new business card design. Our company colours are silver or grey and orange. Feel free to use the white background logo or the black background logo.

Target Market(s)

Local contractors, utility companies, private sector mining/energy companies, developers.

Industry/Entity Type

Telecommunications

Contact Information for Business Card

Each card will need the following info:
Persons name:
Title:
E-mail:
Phone number:
Shop Address:
Mailing Address:

Requirements
Must have
• Each card will need the following info:
• Persons name:
• Title:
• E-mail:
• Phone number:
• Shop Address:
• Mailing Address:

```html
<!DOCTYPE html>
<html lang="en">
<head>
<meta charset="utf-8">
<title>Trenchline Civil Inc — Business Card</title>
<link rel="stylesheet" href="https://fonts.googleapis.com/css2?family=Montserrat:wght@600;700&family=Open+Sans:wght@400&display=swap">
<style>
  :root {
    --backdrop: #e9e7e3;
    --card: #fbfbfb;
    --orange: #ec6625;
    --grey: #5d5e60;
    --silver-dark: #8a8b8d;
    --silver-light: #d4d5d7;
  }
  * { margin: 0; padding: 0; box-sizing: border-box; }
  html, body {
    width: 1200px;
    height: 1022px;
    overflow: hidden;
    background: var(--backdrop);
  }
  .business-card {
    position: absolute;
    left: 100px;
    top: 226px;
    width: 1000px;
    height: 570px;
    background: var(--card);
    border-radius: 22px;
    box-shadow: 0 10px 30px rgba(0,0,0,0.18);
    overflow: hidden;
  }
  .divider-arc {
    position: absolute;
    inset: 0;
  }
  .contact-side {
    position: absolute;
    left: 70px;
    top: 150px;
    font-family: "Open Sans", Arial, sans-serif;
    color: var(--grey);
  }
  .person-name {
    font-family: "Montserrat", Arial, sans-serif;
    font-weight: 600;
    font-size: 34px;
    letter-spacing: 1px;
    color: var(--orange);
    text-transform: uppercase;
  }
  .person-title {
    font-size: 21px;
    margin-top: 2px;
  }
  .address-block {
    font-size: 21px;
    line-height: 30px;
    margin-top: 22px;
  }
  .address-block + .address-block { margin-top: 14px; }
  .address-block.mailing { text-transform: uppercase; }
  .contact-list {
    list-style: none;
    margin-top: 14px;
    font-size: 21px;
    line-height: 30px;
  }
  .contact-list li {
    display: flex;
    align-items: center;
    gap: 12px;
  }
  .contact-icon { width: 18px; height: 18px; flex: none; }
  .brand-side {
    position: absolute;
    right: 70px;
    top: 190px;
    display: flex;
    align-items: center;
    gap: 20px;
  }
  .brand-dot {
    width: 54px;
    height: 54px;
    border-radius: 50%;
    background: var(--orange);
  }
  .brand-name {
    font-family: "Montserrat", Arial, sans-serif;
    font-weight: 700;
    font-size: 44px;
    line-height: 52px;
    color: var(--orange);
    text-transform: uppercase;
  }
</style>
</head>
<body>
  <article class="business-card">
    <svg class="divider-arc" width="1000" height="570" viewBox="0 0 1000 570" aria-hidden="true">
      <path d="M470 0 Q620 285 470 570" fill="none" stroke="var(--silver-dark)" stroke-width="7"/>
      <path d="M488 0 Q638 285 488 570" fill="none" stroke="var(--silver-light)" stroke-width="4"/>
    </svg>

    <section class="contact-side">
      <h1 class="person-name">Marcus Hale</h1>
      <p class="person-title">Director</p>
      <p class="address-block shop">48 Quarry Lane<br>Fairhaven, NY 12090</p>
      <p class="address-block mailing">PO Box 3150<br>Millbrook, CA 91560</p>
      <ul class="contact-list">
        <li>
          <svg class="contact-icon" viewBox="0 0 18 18"><rect x="4" y="1.5" width="10" height="15" rx="1.5" fill="none" stroke="var(--orange)" stroke-width="1.6"/><circle cx="9" cy="13.5" r="1" fill="var(--orange)"/></svg>
          +330 5550-1842
        </li>
        <li>
          <svg class="contact-icon" viewBox="0 0 18 18"><path d="M4 2 L7 2 L8 6 L6 7.5 Q8 11 10.5 12 L12 10 L16 11 L16 14 Q15 16 12.5 16 Q3 14 2 4.5 Q2 2 4 2Z" fill="var(--orange)"/></svg>
          +330 5550-2937
        </li>
        <li>
          <svg class="contact-icon" viewBox="0 0 18 18"><rect x="1.5" y="3.5" width="15" height="11" fill="none" stroke="var(--orange)" stroke-width="1.6"/><path d="M1.5 3.5 L9 10 L16.5 3.5" fill="none" stroke="var(--orange)" stroke-width="1.6"/></svg>
          info@trenchlinecivil.com
        </li>
        <li>
          <svg class="contact-icon" viewBox="0 0 18 18"><circle cx="9" cy="9" r="7.5" fill="none" stroke="var(--orange)" stroke-width="1.6"/><ellipse cx="9" cy="9" rx="3.2" ry="7.5" fill="none" stroke="var(--orange)" stroke-width="1.3"/><path d="M1.5 9 H16.5" stroke="var(--orange)" stroke-width="1.3"/></svg>
          www.trenchlinecivil.com
        </li>
      </ul>
    </section>

    <section class="brand-side">
      <span class="brand-dot" aria-hidden="true"></span>
      <p class="brand-name">Trenchline<br>Civil Inc</p>
    </section>
  </article>
</body>
</html>
```